New Business Card Design Project

Make a kick ass business card for The Otter Tea Mug, using the designs. I also might like the 2nd place design logo on the back? Maybe all black with that? Not sure. Also, I'm cool with it being on metal, plastic, glass? or whatever for the business card. Maybe shaped like a shark? Let me know what else you need? Would like designs in the next day or so. Thank you.
Target Market(s)
Anyone that is cool
Contact Information for Business Card
Name: Dorian Fenwick
Phone: 317.594.8126
inventor/creator/entrepreneur/owner
www.theottertyeamug.example
social media links
https://www.facebook.com/theottertyeamug
https://twitter.com/otter_brew
https://www.instagram.com/theottertyeamug/
I'll get the Pinterest one soon
Colors
Designer to choose colors to be used in the design.
Requirements
Must have
- The Otter Tea Mug
- www.theottertyeamug.example
- social media tags?
- My logos and picture/photo of wine glass
Nice to have
- Maybe shaped like a wine glass or shark
- I'll let you decide but my same colors from my website would be nice

```html
<!DOCTYPE html>
<html lang="en">
<head>
<meta charset="utf-8">
<title>The Otter Tea Mug – Business Card</title>
<link rel="stylesheet" href="https://fonts.googleapis.com/css2?family=Montserrat:wght@300;400&display=swap">
<style>
  :root {
    --backdrop: #5b4134;
    --card-light: #ebebeb;
    --card-dark: #2a2c2c;
    --ink-grey: #6f6f6f;
    --ink-body: #4a4a4a;
    --brand-red: #b3262f;
    --brand-red-soft: #d46a70;
    --emboss-mark: #1c1e1e;
    --emboss-text: #4a4d4d;
    --glass-tone-a: #f6f6f6;
    --glass-tone-b: #dcdcdc;
  }
  html, body {
    margin: 0;
    width: 1200px;
    height: 1000px;
    overflow: hidden;
    background: var(--backdrop);
    font-family: "Montserrat", "Helvetica Neue", Arial, sans-serif;
  }
  .canvas { position: relative; width: 1200px; height: 1000px; }

  .card-front {
    position: absolute; left: 44px; top: 170px;
    width: 398px; height: 665px;
    background: var(--card-light);
    text-align: center;
    overflow: hidden;
  }
  .front-mark {
    position: absolute; left: 119px; top: 36px;
    width: 160px; height: 50px;
    border-radius: 50%;
    background: linear-gradient(90deg, var(--brand-red-soft), var(--brand-red));
  }
  .brand-name {
    position: absolute; left: 0; right: 0; top: 98px;
    font-size: 33px; font-weight: 300; color: var(--ink-grey);
    margin: 0; line-height: 40px;
  }
  .person-name {
    position: absolute; left: 0; right: 0; top: 163px;
    font-size: 22px; font-weight: 400; color: var(--brand-red);
    letter-spacing: 0.5px; margin: 0; line-height: 28px;
  }
  .person-title {
    position: absolute; left: 0; right: 0; top: 190px;
    font-size: 16px; font-weight: 300; color: var(--ink-body); margin: 0;
    line-height: 22px;
  }
  .contact-list {
    position: absolute; left: 0; right: 0; top: 223px;
    list-style: none; margin: 0; padding: 0;
    font-size: 16px; font-weight: 300; color: var(--ink-body);
    line-height: 23px;
  }
  .social-list {
    position: absolute; left: 0; right: 0; top: 297px;
    list-style: none; margin: 0; padding: 0;
    font-size: 16px; font-weight: 300; color: var(--ink-body);
    line-height: 24px;
  }
  .social-dot {
    display: inline-block; width: 15px; height: 15px; border-radius: 50%;
    background: var(--brand-red); vertical-align: -2px; margin-right: 6px;
  }
  .glass-art {
    position: absolute; left: 84px; top: 370px;
    width: 232px; height: 295px;
    background: linear-gradient(180deg, var(--glass-tone-a), var(--glass-tone-b));
    border-radius: 0 0 110px 110px;
  }

  .card-back {
    position: absolute; left: 491px; top: 305px;
    width: 667px; height: 395px;
    background: var(--card-dark);
  }
  .back-mark {
    position: absolute; left: 227px; top: 130px;
    width: 187px; height: 62px;
    border-radius: 50%;
    background: var(--emboss-mark);
  }
  .back-wordmark {
    position: absolute; left: 0; right: 0; top: 222px;
    text-align: center; margin: 0;
    font-size: 46px; font-weight: 300; color: var(--emboss-text);
    line-height: 52px;
  }
</style>
</head>
<body>
<main class="canvas">
  <section class="card-front">
    <div class="front-mark" role="img" aria-label="Brand symbol in red dotted tones"></div>
    <h1 class="brand-name">Otter Tea Mug</h1>
    <p class="person-name">Dorian Fenwick</p>
    <p class="person-title">inventor/creator/entrepreneur/owner</p>
    <ul class="contact-list">
      <li>317.594.8126</li>
      <li>info@theottertyeamug.example</li>
      <li>www.theottertyeamug.example</li>
    </ul>
    <ul class="social-list">
      <li><span class="social-dot"></span>theottertyeamug</li>
      <li><span class="social-dot"></span>otter_brew</li>
    </ul>
    <div class="glass-art" role="img" aria-label="Embossed outline of a wine glass holding the brand symbol"></div>
  </section>

  <section class="card-back">
    <div class="back-mark" role="img" aria-label="Blind-embossed brand symbol"></div>
    <p class="back-wordmark">The Otter Tea Mug</p>
  </section>
</main>
</body>
</html>
```